Wild Mo's Wine Label Project

We need a new entry level wine label called "Wild Mo's" for a range of wines we are developing from inland Australia. Our company is made up of three youngish guys who live hard and love taking the mickey. Wild Mo is Wild Moss - the largest and loudest of the three partners (and ideally this label will take the mickey out of him). We've grown the grapes ourselves for this first release which will be a 2012 Pinot Gris. Wine style is dry, young, fresh and contemporary and pitched at the sub AUD $10 retail price point. The package will be flint (clear) claret shape bottle with plain screwcap (colour matched to suit the winning label design).

I've attached a couple of photos of Wild Moss to give you some idea of his presence and persona.

Target Market(s)

Semi educated 25 - 40 year old wine drinkers. Skewed towards females.

Industry/Entity Type

Retail

Requirements
Should not have
• Anything traditional or old fashioned

```html
<!DOCTYPE html>
<html lang="en">
<head>
<meta charset="utf-8">
<title>Wild Mo's Pinot Gris Label</title>
<link href="https://fonts.googleapis.com/css2?family=Saira+Condensed:wght@600;700&family=Exo+2:wght@700&family=Pixelify+Sans:wght@700&family=Didact+Gothic&display=swap" rel="stylesheet">
<style>
  :root {
    --rust: #a3410f;
    --rust-deep: #8e2c05;
    --ink: #0c0a08;
    --white: #ffffff;
  }
  html, body {
    margin: 0;
    padding: 0;
    width: 848px;
    height: 1200px;
    overflow: hidden;
    background: var(--rust);
  }
  .label {
    position: relative;
    width: 848px;
    height: 1200px;
    overflow: hidden;
    background: var(--rust);
  }
  .leaf-pattern {
    position: absolute;
    inset: 0;
    background: radial-gradient(ellipse at 30% 25%, var(--rust-deep) 0%, var(--rust) 45%, var(--rust) 100%);
  }
  .brand-name {
    position: absolute;
    left: 18px;
    top: 30px;
    margin: 0;
    font-family: "Saira Condensed", sans-serif;
    font-weight: 700;
    font-size: 290px;
    line-height: 0.9;
    color: var(--white);
    text-transform: uppercase;
  }
  .volume {
    position: absolute;
    left: 80px;
    top: 712px;
    margin: 0;
    font-family: "Exo 2", sans-serif;
    font-weight: 700;
    font-size: 88px;
    line-height: 1;
    color: var(--white);
  }
  .vintage {
    position: absolute;
    right: 18px;
    top: 650px;
    margin: 0;
    font-family: "Saira Condensed", sans-serif;
    font-weight: 600;
    font-size: 76px;
    line-height: 1;
    color: var(--white);
    letter-spacing: 1px;
  }
  .variety {
    position: absolute;
    right: 16px;
    top: 716px;
    margin: 0;
    font-family: "Pixelify Sans", sans-serif;
    font-weight: 700;
    font-size: 80px;
    line-height: 1;
    color: var(--ink);
    letter-spacing: 2px;
  }
  .origin {
    position: absolute;
    left: 12px;
    top: 1044px;
    margin: 0;
    font-family: "Didact Gothic", sans-serif;
    font-size: 48px;
    line-height: 1;
    color: var(--ink);
    letter-spacing: 8px;
  }
  .alcohol {
    position: absolute;
    left: 10px;
    top: 1106px;
    margin: 0;
    font-family: "Saira Condensed", sans-serif;
    font-weight: 700;
    font-size: 40px;
    line-height: 1;
    color: var(--white);
  }
  .producer {
    position: absolute;
    left: 12px;
    top: 1152px;
    margin: 0;
    font-family: "Didact Gothic", sans-serif;
    font-size: 28px;
    line-height: 1;
    color: var(--ink);
    letter-spacing: 6px;
  }
</style>
</head>
<body>
  <main class="label">
    <div class="leaf-pattern" role="img" aria-label="Faint vine leaves and tendrils scattered over a rust background"></div>

    <h1 class="brand-name">Wild<br>Mo's</h1>

    <p class="volume">750</p>
    <p class="vintage">VINTAGE 2012</p>
    <p class="variety">pinot gris</p>

    <p class="origin">wine of australia</p>
    <p class="alcohol">ALCOHOL 12.0%</p>
    <p class="producer">amber thursday</p>
  </main>
</body>
</html>
```